Webdesign für ein Dachdeckerbetrieb
Zielgruppe
Wir sind ein Dachdeckerbetrieb.
Zielgruppe sind öffentliche Auftrageber , Hausverwaltungen und private Hausbesitzer.
Aufgabenstellung
Die Seite sollte übersichtlich sein. Nicht zuviele Menüs durch die man klicken muss.
Bilder können wir liefern .
Nach Vorgabe des Designers beschaffen wir die Bilder .
Logo ist vorhanden.

```html
<!DOCTYPE html>
<html lang="de">
<head>
<meta charset="utf-8">
<title>Kranzler Dachbau – Webdesign Übersicht</title>
<link href="https://fonts.googleapis.com/css2?family=Nunito:wght@600;700;800&family=Roboto:wght@400;500;700&display=swap" rel="stylesheet">
<style>
:root{
  --blue:#1c4fc4;
  --blue-deep:#1642ad;
  --navy:#0c1c43;
  --ink:#111b2b;
  --text:#2a2f3a;
  --muted:#6b7280;
  --pale:#e6ecf8;
  --line:#e4e7ee;
  --purple:#1a1550;
  --white:#ffffff;
}
*{box-sizing:border-box;margin:0;padding:0}
html,body{width:1066px;height:1200px;overflow:hidden;background:#fff}
body{position:relative;font-family:"Roboto",sans-serif;color:var(--text)}
.abs{position:absolute}
.h{font-family:"Nunito",sans-serif}

.hdr{position:absolute;width:272px;height:40px}
.hdr .brand{position:absolute;left:10px;font:700 8px/1 "Roboto",sans-serif;color:var(--navy);letter-spacing:.3px;display:flex;align-items:center;gap:3px}
.hdr .brand i{display:block;width:7px;height:7px;background:#7ab51d}
.hdr .brand small{display:block;font-size:3.5px;letter-spacing:2px;font-weight:700}
.hdr nav{position:absolute;right:14px;display:flex;gap:10px;font:500 4.3px "Roboto",sans-serif;color:var(--ink)}
.social{position:absolute;display:flex;gap:5px}
.social span{width:3px;height:3px;border-radius:50%;background:var(--ink)}
.social.light span{background:#fff}

.features{position:absolute;width:272px;height:218px;background:linear-gradient(180deg,var(--blue) 55%,#1846b8);color:#fff;overflow:hidden}
.feat{position:absolute;top:0;width:90px;text-align:center}
.feat .num{position:absolute;top:58px;width:100%;font:800 28px "Nunito",sans-serif;color:rgba(255,255,255,.07)}
.feat .ic{position:absolute;top:81px;left:28px;width:34px;height:34px;border-radius:50%;background:#fff;display:flex;align-items:center;justify-content:center}
.feat h4{position:absolute;top:124px;width:100%;font:700 6px "Nunito",sans-serif}
.feat p{position:absolute;top:139px;left:3px;right:3px;font:400 4px/7.4px "Roboto",sans-serif}
.feat a{display:block;margin-top:3px;font-weight:700;color:#fff;text-decoration:none}

.foot{position:absolute;width:272px;background:var(--navy);color:#fff}
.foot .item{position:absolute;top:15px;display:flex;gap:5px;align-items:center}
.foot .dot{width:10px;height:10px;border-radius:50%;background:var(--blue);display:flex;align-items:center;justify-content:center}
.foot .item small{display:block;font:400 4px "Roboto",sans-serif;opacity:.8}
.foot .item b{display:block;font:700 4.6px "Roboto",sans-serif}
.foot .sep{position:absolute;top:14px;width:1px;height:16px;background:rgba(255,255,255,.12)}
.foot .bar{position:absolute;left:0;right:0;border-top:1px solid rgba(255,255,255,.1)}
.foot .copy{position:absolute;right:9px;font:400 4px "Roboto",sans-serif}

.ph{position:absolute}
.small{font:400 3.9px/7.4px "Roboto",sans-serif;color:var(--muted)}
.kick{font:700 4.2px "Roboto",sans-serif;color:var(--ink);text-transform:uppercase}
.btn{position:absolute;display:flex;align-items:center;justify-content:center;font:700 4.3px "Roboto",sans-serif;color:#fff;background:var(--blue);border-radius:2px}
.card{position:absolute;background:#fff;border:1px solid var(--line)}
.card h5{position:absolute;left:6px;top:36px;font:700 4.4px "Roboto",sans-serif;color:var(--ink)}
.card p{position:absolute;left:6px;right:6px;top:45px;font:400 4px/7.4px "Roboto",sans-serif;color:var(--muted)}
.card .go{position:absolute;left:6px;width:8px;height:8px;border-radius:50%;background:var(--pale);color:var(--blue);font-size:5px;display:flex;align-items:center;justify-content:center}
.check{display:flex;align-items:center;gap:3px;font:400 4.2px "Roboto",sans-serif}
.check i{width:7px;height:7px;border-radius:50%;background:var(--blue);display:inline-flex;align-items:center;justify-content:center}
</style>
</head>
<body>

<svg width="0" height="0" style="position:absolute">
  <defs>
    <symbol id="i-chat" viewBox="0 0 24 24"><path d="M3 6h12v8H8l-3 3v-3H3z M17 9h4v8h-2v3l-3-3h-5v-2" fill="none" stroke="#1c4fc4" stroke-width="1.4"/></symbol>
    <symbol id="i-pen" viewBox="0 0 24 24"><path d="M12 3v6 M7 10l5-1 5 1-3 7h-4z M10 21h4v-4h-4z M3 8h4 M17 8h4" fill="none" stroke="#1c4fc4" stroke-width="1.4"/><circle cx="12" cy="13" r="1.3" fill="#1c4fc4"/></symbol>
    <symbol id="i-thumb" viewBox="0 0 24 24"><path d="M4 11h4v9H4z M8 12l4-7c2 0 2 2 1.5 4H19c1.5 0 2 1.5 1.5 3l-2 6c-.4 1-1 2-2 2H8" fill="none" stroke="#1c4fc4" stroke-width="1.4"/><path d="M16 2v2 M19 3l-1 2 M21 6h-2" stroke="#1c4fc4" stroke-width="1.2"/></symbol>
    <symbol id="i-phone" viewBox="0 0 24 24"><path d="M6 3l4 4-2 2c1 3 4 6 7 7l2-2 4 4-3 3C10 20 4 14 3 6z" fill="#fff"/></symbol>
    <symbol id="i-mail" viewBox="0 0 24 24"><path d="M3 6h18v12H3z" fill="#fff"/><path d="M3 6l9 7 9-7" fill="none" stroke="#1c4fc4" stroke-width="1.6"/></symbol>
    <symbol id="i-mailb" viewBox="0 0 24 24"><path d="M3 6h18v12H3z" fill="#1c4fc4"/><path d="M3 6l9 7 9-7" fill="none" stroke="#fff" stroke-width="1.6"/></symbol>
    <symbol id="i-clock" viewBox="0 0 24 24"><circle cx="12" cy="12" r="9" fill="#fff"/><path d="M12 7v5l3 2" fill="none" stroke="#1c4fc4" stroke-width="2"/></symbol>
    <symbol id="i-screen" viewBox="0 0 24 24"><path d="M3 4h18v12H3z M9 20h6 M12 16v4 M6 7h6 M6 10h4 M14 8h4v5h-4z" fill="none" stroke="#1c4fc4" stroke-width="1.2"/></symbol>
    <symbol id="i-tick" viewBox="0 0 24 24"><path d="M5 12l5 5 9-10" fill="none" stroke="#fff" stroke-width="3"/></symbol>
    <symbol id="i-tickb" viewBox="0 0 24 24"><path d="M5 12l5 5 9-10" fill="none" stroke="#1c4fc4" stroke-width="3"/></symbol>
  </defs>
</svg>

<!-- ===== Column 1: Über uns ===== -->
<div class="social" style="left:271px;top:6px"><span></span><span></span><span></span></div>
<header class="hdr" style="left:34px;top:14px;border-bottom:1px solid #222;height:30px">
  <div class="brand" style="top:10px"><i></i><div>KRANZLER<small>DACHBAU</small></div></div>
  <nav style="top:13px"><span>Über Uns</span><span>Referenzen</span><span>Leistungen</span><span>Kontakt</span></nav>
</header>

<div class="ph" role="img" aria-label="Foto: Arbeitsplatz mit Laptop in violettem Licht" style="left:37px;top:76px;width:97px;height:110px;background:linear-gradient(135deg,#1c1f46,#6a2c8f 60%,#2b2f6e)"></div>
<div class="ph" role="img" aria-label="Foto: Team bespricht Pläne am Tisch" style="left:70px;top:138px;width:98px;height:86px;background:linear-gradient(135deg,#cfc8c0,#8a7a6e 55%,#b84a48)"></div>
<div class="abs" style="left:173px;top:86px;width:130px">
  <div class="kick" style="text-transform:none">It Support For Business</div>
  <p style="margin-top:6px;font:500 4.1px/7.2px Roboto,sans-serif;color:var(--ink)">Als Dachdecker-Meisterbetrieb sind wir der richtige Ansprechpartner für alle Arbeiten rund um ein fachgerechtes Dach, sowohl im privaten als auch im gewerblichen Bereich.</p>
  <p class="small" style="margin-top:6px">Wir helfen Ihnen persönliche Wünsche mit technisch und fachlich richtigen Lösungen umzusetzen, egal ob Sie eine Neueindeckung oder eine Sanierung Ihres Wohnhauses wünschen, ob eine Wärmedämmung nach den neuesten gesetzlichen Vorgaben umgesetzt werden soll, ein Dachfenster eingebaut oder ersetzt werden soll oder eine Reparatur ansteht.</p>
  <p class="small" style="margin-top:5px">Schauen Sie sich auf unserer Internetseite um und lernen Sie die Vielfältigkeit und die umfassenden Tätigkeiten des Dachdeckerhandwerks kennen.</p>
</div>
<div class="btn" style="left:173px;top:205px;width:127px;height:18px;background:var(--ink)">Kontaktieren Sie uns für weitere Informationen</div>

<section class="features" style="left:34px;top:261px">
  <div class="feat" style="left:0"><div class="num">01</div><div class="ic"><svg width="20" height="20"><use href="#i-chat"/></svg></div><h4>Finanzverwaltung</h4><p>Sie suchen starke und zuverlässige Dachdecker oder Zimmerer für Ihre Dachsanierung?<a>Begleiten Sie uns →</a></p></div>
  <div class="feat" style="left:91px"><div class="num">02</div><div class="ic"><svg width="20" height="20"><use href="#i-pen"/></svg></div><h4>Projektnachverfolgung</h4><p>Unsere Dachdecker und Zimmerer bauen Ihnen ein qualitativ hochwertiges Dach, das Sie bei „Wind und Wetter“ schützt und Ihnen ein sicheres und langlebiges Zuhause bietet.<a>Begleiten Sie uns →</a></p></div>
  <div class="feat" style="left:182px"><div class="num">01</div><div class="ic"><svg width="20" height="20"><use href="#i-thumb"/></svg></div><h4>Gruppenerfolg</h4><p>HERZLICH WILLKOMMEN – WIR ARBEITEN AUS ÜBERZEUGUNG UND FREUDE AM TUN!<a>Begleiten Sie uns →</a></p></div>
</section>
<section class="abs" style="left:34px;top:479px;width:272px;height:102px;background:var(--pale);text-align:center">
  <div class="abs" style="left:0;width:90px;top:38px"><div class="h" style="font-size:13px;font-weight:700;color:var(--blue)">24+</div><div style="font:700 5.3px Roboto,sans-serif;color:var(--ink);margin-top:2px">Auszeichnungen gewonnen</div></div>
  <div class="abs" style="left:91px;width:90px;top:38px"><div class="h" style="font-size:13px;font-weight:700;color:var(--blue)">12+</div><div style="font:700 5.3px Roboto,sans-serif;color:var(--ink);margin-top:2px">Jahre Erfahrung</div></div>
  <div class="abs" style="left:182px;width:90px;top:38px"><div class="h" style="font-size:13px;font-weight:700;color:var(--blue)">352+</div><div style="font:700 5.3px Roboto,sans-serif;color:var(--ink);margin-top:2px">Zufriedene Kunden</div></div>
</section>
<footer class="foot" style="left:34px;top:581px;height:93px">
  <div class="item" style="left:10px"><span class="dot"><svg width="6" height="6"><use href="#i-phone"/></svg></span><div><small>Telefon-Nr</small><b>01234 - 56 78 90</b></div></div>
  <div class="sep" style="left:93px"></div>
  <div class="item" style="left:98px"><span class="dot"><svg width="6" height="6"><use href="#i-mail"/></svg></span><div><small>Email</small><b>info@kranzler-dach.example</b></div></div>
  <div class="sep" style="left:200px"></div>
  <div class="item" style="left:202px"><span class="dot"><svg width="6" height="6"><use href="#i-clock"/></svg></span><div><small>stündlich</small><b>9:00 - 7:00</b></div></div>
  <div class="bar" style="top:74px"></div>
  <div class="social light" style="left:10px;top:82px"><span></span><span></span><span></span><span></span></div>
  <div class="copy" style="top:81px">© Copyright 2022 kranzler-dach.example</div>
</footer>

<!-- ===== Column 1: Kontakt ===== -->
<div class="social" style="left:271px;top:717px"><span></span><span></span><span></span></div>
<header class="hdr" style="left:34px;top:725px;border-bottom:1px solid #222;height:30px">
  <div class="brand" style="top:10px"><i></i><div>KRANZLER<small>DACHBAU</small></div></div>
  <nav style="top:13px"><span>Über Uns</span><span>Referenzen</span><span>Leistungen</span><span>Kontakt</span></nav>
</header>
<div class="abs" style="left:38px;top:787px;width:264px;height:83px;border:3px solid #eef0f4;text-align:center;font:400 3.8px/7px Roboto,sans-serif;color:var(--muted)">
  <div class="abs" style="left:8px;width:70px;top:14px"><svg width="12" height="12" viewBox="0 0 24 24"><path d="M12 2a6 6 0 0 0-6 6c0 5 6 11 6 11s6-6 6-11a6 6 0 0 0-6-6z" fill="#1c4fc4"/><circle cx="12" cy="8" r="2" fill="#fff"/><path d="M2 22l4-8h12l4 8z" fill="none" stroke="#1c4fc4" stroke-width="1.5"/></svg><div style="margin-top:2px">Kranzler Dachbau<br>Lindenweg 7<br>12345 Musterdorf</div></div>
  <div class="abs" style="left:93px;width:80px;top:14px"><svg width="12" height="12"><use href="#i-mailb"/></svg><div style="margin-top:2px;font-style:italic;font-family:serif">Jonas, Lea, Timo, Anke<br>Wendlandt &amp; Team<br>holzbau-wendlandt@<br>post.example</div></div>
  <div class="abs" style="left:186px;width:70px;top:14px"><svg width="12" height="12" viewBox="0 0 24 24"><path d="M6 3l4 4-2 2c1 3 4 6 7 7l2-2 4 4-3 3C10 20 4 14 3 6z" fill="none" stroke="#1c4fc4" stroke-width="1.5"/></svg><div style="margin-top:2px">01234 - 56 78 90</div></div>
</div>
<div class="ph" role="img" aria-label="Foto: lächelnde Kundin mit blauer Farbfläche" style="left:37px;top:891px;width:89px;height:141px;background:linear-gradient(160deg,#6e8ede,#2b55c6 70%,#2049b8)"></div>
<div class="abs h" style="left:41px;top:993px;font:700 11.5px/12px Nunito,sans-serif;color:#fff">Leave A<br>Message</div>
<div class="abs" style="left:134px;top:891px;width:170px">
  <div class="h" style="font:600 8px Nunito,sans-serif;color:var(--ink)">Eine Nachricht schicken</div>
  <p class="small" style="margin-top:3px">Vermeidet Vergnügen selbst, weil es Vergnügen ist, sondern weil diejenigen, die nicht wissen, wie man Vergnügen verfolgt</p>
</div>
<div class="abs small" style="left:137px;top:934px;width:78px;height:18px;border:1px solid var(--line);padding:3px 4px;font-size:3.6px">Your Full Name</div>
<div class="abs small" style="left:221px;top:934px;width:78px;height:18px;border:1px solid var(--line);padding:3px 4px;font-size:3.6px">Your Email</div>
<div class="abs small" style="left:137px;top:959px;width:162px;height:50px;border:1px solid var(--line);padding:3px 4px;font-size:3.6px">Write Message</div>
<div class="btn" style="left:137px;top:1017px;width:51px;height:15px;font-weight:500">Send Message</div>
<footer class="foot" style="left:34px;top:1064px;height:93px">
  <div class="item" style="left:10px"><span class="dot"><svg width="6" height="6"><use href="#i-phone"/></svg></span><div><small>Telefon-Nr</small><b>01234 - 56 78 90</b></div></div>
  <div class="sep" style="left:93px"></div>
  <div class="item" style="left:98px"><span class="dot"><svg width="6" height="6"><use href="#i-mail"/></svg></span><div><small>Email</small><b>info@kranzler-dach.example</b></div></div>
  <div class="sep" style="left:200px"></div>
  <div class="item" style="left:202px"><span class="dot"><svg width="6" height="6"><use href="#i-clock"/></svg></span><div><small>stündlich</small><b>9:00 - 7:00</b></div></div>
  <div class="bar" style="top:74px"></div>
  <div class="social light" style="left:10px;top:82px"><span></span><span></span><span></span><span></span></div>
  <div class="copy" style="top:81px">© Copyright 2022 kranzler-dach.example</div>
</footer>

<!-- ===== Column 2: Startseite ===== -->
<div class="abs" style="left:399px;top:17px;width:75px;height:39px;background:#f1f2f5"></div>
<header class="hdr" style="left:399px;top:17px;height:39px">
  <div class="brand" style="top:15px"><i></i><div>KRANZLER<small>DACHBAU</small></div></div>
  <nav style="top:18px;right:64px"><span>Über Uns</span><span>Referenzen</span><span>Leistungen</span><span>Kontakt</span></nav>
</header>
<section class="abs" style="left:399px;top:56px;width:272px;height:176px;overflow:hidden;text-align:center;color:#fff">
  <div class="ph" role="img" aria-label="Foto: Team in Besprechung am Laptop, blau eingefärbt" style="left:0;top:0;width:272px;height:176px;background:linear-gradient(135deg,#3a4a8c,#2a3a84 50%,#1f2d6e)"></div>
  <div class="abs" style="left:0;right:0;top:29px;font:500 4.6px Roboto,sans-serif">STÄRKEN SIE IHR UNTERNEHMEN</div>
  <div class="abs h" style="left:40px;right:40px;top:40px;font:600 19px/19px Nunito,sans-serif">Exzellente IT-Services für Ihren Erfolg</div>
  <div class="btn" style="left:111px;top:106px;width:49px;height:15px">Arbeite mit uns</div>
</section>

<div class="card" style="left:403px;top:265px;width:128px;height:91px">
  <svg class="abs" style="left:5px;top:7px" width="20" height="20"><use href="#i-screen"/></svg>
  <h5>Product Service</h5><p>Als Dachdecker-Meisterbetrieb sind wir der richtige Ansprechpartner für alle Arbeiten rund um ein fachgerechtes Dach</p><span class="go" style="top:74px">→</span>
</div>
<div class="card" style="left:539px;top:265px;width:128px;height:84px">
  <svg class="abs" style="left:5px;top:7px" width="20" height="20"><use href="#i-screen"/></svg>
  <h5>IT Management</h5><p>Wir helfen Ihnen persönliche Wünsche mit technisch und fachlich richtigen Lösungen umzusetzen</p><span class="go" style="top:67px">→</span>
</div>
<div class="card" style="left:403px;top:365px;width:128px;height:82px">
  <svg class="abs" style="left:5px;top:7px" width="20" height="20"><use href="#i-screen"/></svg>
  <h5>Cloud Services</h5><p>ob eine Wärmedämmung nach den neuesten gesetzlichen Vorgaben umgesetzt werden soll</p><span class="go" style="top:66px">→</span>
</div>
<div class="card" style="left:539px;top:365px;width:128px;height:90px">
  <svg class="abs" style="left:5px;top:7px" width="20" height="20"><use href="#i-screen"/></svg>
  <h5>Machine Learning</h5><p>Solides Handwerk und Können ist eine Sache, Vertrauen eine andere.Sie stellen uns Aufgaben und wir lösen diese individuell.</p><span class="go" style="top:74px">→</span>
</div>

<section class="abs" style="left:399px;top:488px;width:272px;height:229px;background:var(--ink);color:#fff;overflow:hidden">
  <div class="abs" style="left:6px;top:33px;width:125px;height:136px;border-radius:55% 45% 50% 50%/50% 50% 50% 50%;background:var(--blue)"></div>
  <div class="ph" role="img" aria-label="Foto: Team mit Tablet und Bauplänen" style="left:11px;top:33px;width:120px;height:136px;border-radius:55% 45% 50% 50%/50% 50% 50% 50%;background:linear-gradient(135deg,#e6e2de,#a99486 50%,#cfd6e0)"></div>
  <div class="abs" style="left:139px;top:38px;width:110px">
    <div style="font:700 4.2px Roboto,sans-serif">Es unterstützt das Geschäft</div>
    <div class="h" style="margin-top:5px;font:600 9.4px/12.4px Nunito,sans-serif">Bereiten Sie sich mit IT-Lösungen auf Ihren Geschäftserfolg vor</div>
    <p style="margin-top:6px;font:400 4px/7.5px Roboto,sans-serif;color:#c8cdd6">Wir helfen Ihnen persönliche Wünsche mit technisch und fachlich richtigen Lösungen umzusetzen, egal ob Sie eine Neueindeckung oder eine Sanierung Ihres Wohnhauses wünschen, ob eine Wärmedämmung nach den neuesten gesetzlichen Vorgaben umgesetzt werden soll, ein Dachfenster eingebaut oder ersetzt werden soll oder eine Reparatur ansteht.</p>
  </div>
  <div class="abs check" style="left:139px;top:161px"><i><svg width="4" height="4"><use href="#i-tick"/></svg></i>Ziegeldach</div>
  <div class="abs check" style="left:202px;top:161px"><i><svg width="4" height="4"><use href="#i-tick"/></svg></i>Flachdach</div>
  <div class="abs check" style="left:139px;top:177px"><i><svg width="4" height="4"><use href="#i-tick"/></svg></i>Abdichtungstechnik</div>
  <div class="abs check" style="left:202px;top:177px"><i><svg width="4" height="4"><use href="#i-tick"/></svg></i>Reparaturen &amp; Wartung</div>
</section>

<section class="abs" style="left:399px;top:717px;width:272px;height:213px;overflow:hidden">
  <div class="abs" style="left:0;top:0;width:214px;height:213px;background:linear-gradient(135deg,#eeeaf7,#f6f4fb)"></div>
  <div class="abs" style="left:214px;top:0;width:58px;height:213px;background:var(--purple)"></div>
  <div class="abs" style="left:3px;top:31px;width:267px;height:155px;background:var(--blue);color:#fff">
    <div class="abs" style="left:11px;top:20px;font:700 4.2px Roboto,sans-serif">IMMER UM DICH ZUFRIEDEN ZU STELLEN</div>
    <div class="abs h" style="left:11px;top:29px;width:150px;font:600 9.4px/12.4px Nunito,sans-serif">Wir beschäftigen uns mit den Aspekten des Fachlichen</div>
    <div class="abs" style="left:202px;top:27px;width:53px;height:16px;border:1px solid rgba(255,255,255,.6);font:700 4.2px Roboto,sans-serif;display:flex;align-items:center;justify-content:center">Begleiten Sie uns</div>
    <div class="abs" style="left:27px;top:70px;width:36px;height:36px;border-radius:50%;background:rgba(255,255,255,.16)"></div>
    <div class="abs" style="left:116px;top:70px;width:36px;height:36px;border-radius:50%;background:rgba(255,255,255,.16)"></div>
    <div class="abs" style="left:205px;top:70px;width:36px;height:36px;border-radius:50%;background:rgba(255,255,255,.16)"></div>
    <svg class="abs" style="left:35px;top:78px" width="20" height="20" viewBox="0 0 24 24"><path d="M3 6h12v8H8l-3 3v-3H3z M17 9h4v8h-2v3l-3-3h-5v-2" fill="none" stroke="#fff" stroke-width="1.4"/></svg>
    <svg class="abs" style="left:124px;top:78px" width="20" height="20" viewBox="0 0 24 24"><path d="M12 3v6 M7 10l5-1 5 1-3 7h-4z M10 21h4v-4h-4z M3 8h4 M17 8h4" fill="none" stroke="#fff" stroke-width="1.4"/></svg>
    <svg class="abs" style="left:213px;top:78px" width="20" height="20" viewBox="0 0 24 24"><path d="M4 11h4v9H4z M8 12l4-7c2 0 2 2 1.5 4H19c1.5 0 2 1.5 1.5 3l-2 6c-.4 1-1 2-2 2H8" fill="none" stroke="#fff" stroke-width="1.4"/></svg>
    <span class="abs" style="left:56px;top:70px;width:8px;height:8px;border-radius:50%;background:#fff;color:var(--blue);font:700 4.5px/8px Roboto,sans-serif;text-align:center">1</span>
    <span class="abs" style="left:145px;top:70px;width:8px;height:8px;border-radius:50%;background:#fff;color:var(--blue);font:700 4.5px/8px Roboto,sans-serif;text-align:center">2</span>
    <span class="abs" style="left:234px;top:70px;width:8px;height:8px;border-radius:50%;background:#fff;color:var(--blue);font:700 4.5px/8px Roboto,sans-serif;text-align:center">3</span>
    <div class="abs" style="left:0;width:90px;top:113px;text-align:center;font:700 5.6px/8px Nunito,sans-serif">Hören Sie sich Ihre Projekte an</div>
    <div class="abs" style="left:89px;width:90px;top:113px;text-align:center;font:700 5.6px/8px Nunito,sans-serif">beste Verlobung</div>
    <div class="abs" style="left:178px;width:90px;top:113px;text-align:center;font:700 5.6px/8px Nunito,sans-serif">Erfolg genehmigt</div>
  </div>
</section>
<footer class="foot" style="left:399px;top:930px;height:53px">
  <div class="item" style="left:6px;top:12px"><span class="dot"><svg width="6" height="6"><use href="#i-phone"/></svg></span><div><small>Telefon-Nr</small><b>01234 - 56 78 90</b></div></div>
  <div class="sep" style="left:93px;top:11px"></div>
  <div class="item" style="left:100px;top:12px"><span class="dot"><svg width="6" height="6"><use href="#i-mail"/></svg></span><div><small>Email</small><b>info@kranzler-dach.example</b></div></div>
  <div class="sep" style="left:200px;top:11px"></div>
  <div class="item" style="left:211px;top:12px"><span class="dot"><svg width="6" height="6"><use href="#i-clock"/></svg></span><div><small>stündlich</small><b>9:00 - 7:00</b></div></div>
  <div class="bar" style="top:36px"></div>
  <div class="social light" style="left:6px;top:44px"><span></span><span></span><span></span><span></span></div>
  <div class="copy" style="top:43px;right:3px">© Copyright 2022 kranzler-dach.example</div>
</footer>

<!-- ===== Column 3: Leistungen ===== -->
<div class="social" style="left:993px;top:20px"><span></span><span></span><span></span></div>
<header class="hdr" style="left:758px;top:24px;height:33px">
  <div class="brand" style="top:10px"><i></i><div>KRANZLER<small>DACHBAU</small></div></div>
  <nav style="top:18px;right:14px"><span>Über Uns</span><span>Referenzen</span><span>Leistungen</span><span>Kontakt</span></nav>
</header>
<section class="abs" style="left:758px;top:57px;width:272px;height:198px;overflow:hidden;color:#fff">
  <div class="ph" role="img" aria-label="Foto: Geschäftsleute im Gespräch, blau eingefärbt" style="left:0;top:0;width:272px;height:198px;background:linear-gradient(120deg,#23408f,#2a4aa3 55%,#3c5cb4)"></div>
  <div class="abs" style="left:10px;top:62px;font:400 4.6px Roboto,sans-serif">EMPOWER YOUR BUSINESS</div>
  <div class="abs h" style="left:10px;top:74px;width:170px;font:700 19.5px/22px Nunito,sans-serif">Hervorragend für Ihren Erfolg</div>
  <div class="btn" style="left:10px;top:129px;width:50px;height:15px">kontaktiere uns</div>
  <div class="abs" style="left:66px;top:129px;width:15px;height:15px;border-radius:50%;background:#fff;display:flex;align-items:center;justify-content:center"><svg width="6" height="6" viewBox="0 0 10 10"><path d="M2 1l7 4-7 4z" fill="#1c4fc4"/></svg></div>
</section>

<div class="abs" style="left:764px;top:287px;width:113px">
  <div class="kick">IT SUPPORT FOR BUSINESS</div>
  <p style="margin-top:6px;font:400 4.1px/7.3px Roboto,sans-serif;color:var(--ink);text-align:justify">Der Herausforderung ein Steildach, Ziegeldach oder Flachdach fachmännisch zu decken, stellen wir uns täglich gerne.</p>
</div>
<p class="abs small" style="left:897px;top:282px;width:132px">Wir nehmen Ihre Wünsche in unserer anschließenden Planung auf und erarbeiten mit Ihnen und für Sie die optimale Lösung. Unser Leistungsspektrum beinhaltet selbstverständlich auch die Beseitigung und ordnungsgemäße Entsorgung von Asbest. Wir sorgen dafür, dass Sie ein solides und fachmännisch gewartetes Dach haben. Dafür stehen wir mit unserem Namen.</p>

<div class="card" style="left:762px;top:343px;width:129px;height:163px;border-color:#f0f1f4">
  <div class="ph" role="img" aria-label="Foto: Kollegen schauen gemeinsam auf einen Laptop" style="left:5px;top:0;width:118px;height:128px;background:linear-gradient(135deg,#c9bdb0,#6f7f99 60%,#3d4860)"></div>
  <div class="abs" style="left:5px;top:138px;font:500 4px Roboto,sans-serif;color:var(--blue)">Ziegeldach</div>
  <div class="abs" style="left:5px;top:147px;font:400 6.2px Roboto,sans-serif;color:var(--ink)">Flachdach</div>
  <svg class="abs" style="left:105px;top:137px" width="16" height="16"><use href="#i-screen"/></svg>
</div>
<div class="card" style="left:897px;top:343px;width:130px;height:163px;border-color:#f0f1f4">
  <div class="ph" role="img" aria-label="Foto: Frau mit Smartphone und digitalen Symbolen" style="left:7px;top:0;width:118px;height:128px;background:linear-gradient(135deg,#efe7e2,#b48e7a 55%,#5c4a44)"></div>
  <div class="abs" style="left:7px;top:138px;font:500 4px Roboto,sans-serif;color:var(--blue)">Abdichtungstechnik</div>
  <div class="abs" style="left:7px;top:147px;font:400 6.2px Roboto,sans-serif;color:var(--ink)">Reparaturen &amp; Wartung</div>
  <svg class="abs" style="left:108px;top:137px" width="16" height="16"><use href="#i-screen"/></svg>
</div>

<section class="features" style="left:758px;top:570px">
  <div class="feat" style="left:0"><div class="num">01</div><div class="ic"><svg width="20" height="20"><use href="#i-chat"/></svg></div><h4>Advertising and Marketing</h4><p>Unser Fachbetrieb ist Ihr zuverlässiger und fachkundiger Partner in allen Fragen rund um das Thema Bedachungen.<a>Read More →</a></p></div>
  <div class="feat" style="left:91px"><div class="num">02</div><div class="ic"><svg width="20" height="20"><use href="#i-pen"/></svg></div><h4>tägliche Überwachung</h4><p>Wir unterstützen Sie bei der Planung und Durchführung von sämtlichen Dachdeckerarbeiten.<a>Read More →</a></p></div>
  <div class="feat" style="left:182px"><div class="num">01</div><div class="ic"><svg width="20" height="20"><use href="#i-thumb"/></svg></div><h4>Kontrolle des Ergebnisses</h4><p>Bei unserer Arbeit überzeugen vor allem durch fachliche Kompetenz und viel Erfahrung. Wir arbeiten mit Ihnen zusammen – auch in schwindelerregender Höhe.<a>Read More →</a></p></div>
</section>

<div class="abs" style="left:762px;top:820px;width:128px;height:138px;background:#ece8e3"></div>
<div class="ph" role="img" aria-label="Foto: Arbeitsplatz mit Laptop in violettem Licht" style="left:762px;top:821px;width:88px;height:80px;background:linear-gradient(135deg,#1c1f46,#6a2c8f 60%,#2b2f6e)"></div>
<div class="ph" role="img" aria-label="Foto: Team bespricht Pläne am Tisch" style="left:792px;top:878px;width:87px;height:78px;background:linear-gradient(135deg,#cfc8c0,#8a7a6e 55%,#b84a48)"></div>
<div class="abs" style="left:896px;top:820px;width:131px;height:142px;border:1px solid var(--line);padding:5px 2px">
  <div style="font:700 4.2px Roboto,sans-serif;color:var(--blue)">It Support For Business</div>
  <p class="small" style="margin-top:7px;color:var(--text)">Solides Handwerk und Können ist eine Sache, Vertrauen eine andere.<br>Sie stellen uns Aufgaben und wir lösen diese individuell<br>Wir sind Ihr Partner für ausdrucksstarke Dächer.</p>
  <ul style="list-style:none;margin-top:6px;font:400 4px/9.4px Roboto,sans-serif;color:var(--ink)">
    <li><svg width="4" height="4"><use href="#i-tickb"/></svg> Ziegeldach</li>
    <li><svg width="4" height="4"><use href="#i-tickb"/></svg> Flachdach</li>
    <li><svg width="4" height="4"><use href="#i-tickb"/></svg> Abdichtungstechnik</li>
    <li><svg width="4" height="4"><use href="#i-tickb"/></svg> Reparaturen &amp; Wartung</li>
    <li><svg width="4" height="4"><use href="#i-tickb"/></svg> Bauklempnerei</li>
    <li><svg width="4" height="4"><use href="#i-tickb"/></svg> Stehfalzarbeiten</li>
    <li><svg width="4" height="4"><use href="#i-tickb"/></svg> Dacherneuerungen</li>
    <li><svg width="4" height="4"><use href="#i-tickb"/></svg> Dachumbauten</li>
    <li><svg width="4" height="4"><use href="#i-tickb"/></svg> Einbau von Dachflächenfenstern.</li>
  </ul>
</div>
<div class="abs" style="left:896px;top:969px;width:131px;height:19px;background:#3c5aa8;padding:5px 13px;font:500 3.8px/4.2px Roboto,sans-serif;color:#1d47c0">Ein zufriedener Kunde steht bei uns im Mittelpunkt.</div>

<footer class="foot" style="left:758px;top:1007px;height:91px">
  <div class="item" style="left:8px"><span class="dot"><svg width="6" height="6"><use href="#i-phone"/></svg></span><div><small>Telefon-Nr</small><b>01234 - 56 78 90</b></div></div>
  <div class="sep" style="left:90px"></div>
  <div class="item" style="left:98px"><span class="dot"><svg width="6" height="6"><use href="#i-mail"/></svg></span><div><small>Email</small><b>info@kranzler-dach.example</b></div></div>
  <div class="sep" style="left:193px"></div>
  <div class="item" style="left:203px"><span class="dot"><svg width="6" height="6"><use href="#i-clock"/></svg></span><div><small>stündlich</small><b>9:00 - 7:00</b></div></div>
  <div class="social light" style="left:7px;top:82px"><span></span><span></span><span></span><span></span></div>
  <div class="copy" style="top:81px;right:7px">© Copyright 2022 kranzler-dach.example</div>
</footer>

</body>
</html>
```